We are in search of a new business card design for our business. We have a Mexican Grocery Store called Tortilla Grove Market, we would like to see that some have mexican design, but we are open to any type of designs.

Phone: to be announced
Fax: to be announced

Address is:
2415 Calloway Blvd
Dundalk, MD 21222

```html
<!DOCTYPE html>
<html lang="en">
<head>
<meta charset="utf-8">
<title>Tortilla Grove Market – Business Card</title>
<link rel="stylesheet" href="https://fonts.googleapis.com/css2?family=Lato:wght@400;700;900&display=swap">
<style>
  :root {
    --backdrop: #e6dcc8;
    --card-yellow: #f7d51c;
    --card-amber: #f5b531;
    --card-orange: #f39a24;
    --ink: #2f2f33;
    --band-maroon: #a8505a;
    --band-yellow: #f6d423;
  }
  * { margin: 0; padding: 0; box-sizing: border-box; }
  html, body {
    width: 1200px;
    height: 864px;
    overflow: hidden;
    background: var(--backdrop);
  }
  .canvas {
    position: relative;
    width: 1200px;
    height: 864px;
    display: flex;
    align-items: center;
    justify-content: center;
  }
  .card {
    position: relative;
    width: 900px;
    height: 514px;
    background: linear-gradient(115deg, var(--card-yellow) 0%, var(--card-amber) 50%, var(--card-orange) 100%);
    font-family: "Lato", sans-serif;
    color: var(--ink);
    overflow: hidden;
    box-shadow: 0 12px 30px rgba(60, 40, 10, 0.25);
  }
  .card__band {
    position: absolute;
    left: 0;
    top: 0;
    width: 104px;
    height: 100%;
  }
  .card__brand {
    position: absolute;
    left: 50%;
    top: 46%;
    transform: translate(-50%, -50%);
    display: flex;
    align-items: center;
    gap: 18px;
    font-weight: 900;
    font-size: 46px;
    color: var(--ink);
    white-space: nowrap;
  }
  .card__brand-dot {
    width: 28px;
    height: 28px;
    border-radius: 50%;
    background: var(--ink);
  }
  .card__address {
    position: absolute;
    left: 180px;
    bottom: 52px;
    display: flex;
    align-items: flex-end;
    gap: 12px;
    font-size: 26px;
    line-height: 1.25;
  }
  .card__contacts {
    position: absolute;
    right: 44px;
    top: 48px;
    font-size: 26px;
    line-height: 1.35;
    text-align: right;
  }
  .contact-line {
    display: flex;
    align-items: center;
    justify-content: flex-end;
    gap: 12px;
  }
  .icon { width: 22px; height: 22px; flex: none; }
</style>
</head>
<body>
<main class="canvas">
  <section class="card">
    <svg class="card__band" viewBox="0 0 104 514" role="img" aria-label="Mexican-style triangle border pattern in maroon and yellow" preserveAspectRatio="none">
      <rect x="0" y="0" width="104" height="514" fill="var(--band-yellow)"/>
      <rect x="44" y="0" width="52" height="514" fill="var(--band-maroon)"/>
      <line x1="40" y1="0" x2="40" y2="514" stroke="var(--ink)" stroke-width="3"/>
      <line x1="100" y1="0" x2="100" y2="514" stroke="var(--ink)" stroke-width="3"/>
    </svg>

    <div class="card__brand">
      <span class="card__brand-dot"></span>
      <span class="card__brand-name">Tortilla Grove Market</span>
    </div>

    <div class="card__address">
      <svg class="icon" viewBox="0 0 24 24" aria-hidden="true">
        <path d="M12 2a6 6 0 0 0-6 6c0 4.5 6 11 6 11s6-6.5 6-11a6 6 0 0 0-6-6zm0 8.5A2.5 2.5 0 1 1 12 5.5a2.5 2.5 0 0 1 0 5z" fill="var(--ink)"/>
        <ellipse cx="12" cy="21" rx="6" ry="1.6" fill="none" stroke="var(--ink)" stroke-width="1.5"/>
      </svg>
      <p>2415 Calloway Blvd<br>Dundalk, MD 21222</p>
    </div>

    <div class="card__contacts">
      <p class="contact-line">Phone: to be announced
        <svg class="icon" viewBox="0 0 24 24" aria-hidden="true">
          <path d="M6.6 10.8a15 15 0 0 0 6.6 6.6l2.2-2.2a1 1 0 0 1 1-.25 11.4 11.4 0 0 0 3.6.6 1 1 0 0 1 1 1V20a1 1 0 0 1-1 1A17 17 0 0 1 3 4a1 1 0 0 1 1-1h3.5a1 1 0 0 1 1 1c0 1.25.2 2.45.6 3.6a1 1 0 0 1-.25 1z" fill="var(--ink)"/>
        </svg>
      </p>
      <p class="contact-line">Fax: to be announced
        <svg class="icon" viewBox="0 0 24 24" aria-hidden="true">
          <rect x="3" y="8" width="18" height="13" rx="1.5" fill="var(--ink)"/>
          <rect x="7" y="3" width="10" height="6" fill="var(--ink)"/>
          <rect x="6" y="12" width="3" height="2" fill="var(--card-amber)"/>
          <rect x="10.5" y="12" width="3" height="2" fill="var(--card-amber)"/>
          <rect x="15" y="12" width="3" height="2" fill="var(--card-amber)"/>
          <rect x="6" y="16" width="3" height="2" fill="var(--card-amber)"/>
          <rect x="10.5" y="16" width="3" height="2" fill="var(--card-amber)"/>
          <rect x="15" y="16" width="3" height="2" fill="var(--card-amber)"/>
        </svg>
      </p>
    </div>
  </section>
</main>
</body>
</html>
```